Celebrity and Entertainment News Website Needed

Entertainment is one of the favors of Life and I am seeking a standard celebrity website which will discuss in depth news of different celebrities around globe with major focus on American Entertainers. There will be different categories of news from these regions. America, Europe, Asia, Australia and Africa. My website name is quorvella. Youthful colors should be used for the theme and designs, Users should be able to comment at the bottom of each news. Glossy pictures of well know celebrities should be used. Designers can get knowledge from http://tuvrapix.com

Industry/Entity Type

Entertainment

Coding

Coded - Design and coding required

```html
<!DOCTYPE html>
<html lang="en">
<head>
<meta charset="utf-8">
<title>quorvella — Europe</title>
<link href="https://fonts.googleapis.com/css2?family=Open+Sans:wght@400;600;700&display=swap" rel="stylesheet">
<style>
:root{
  --green:#2f9c1e;--yellow:#f4e94a;--bg:#eef0f4;--white:#fff;
  --blue:#2a82c4;--ink:#333;--muted:#8a8f96;--line:#e4e6ea;
  --orange:#c7650b;--purple:#8e5bd1;--dkgreen:#2e7a2c;--navy:#1f35d8;
}
*{box-sizing:border-box;margin:0;padding:0}
html,body{width:1200px;height:3297px;overflow:hidden}
body{background:var(--bg);font-family:"Open Sans",Arial,sans-serif;color:var(--ink);position:relative}
.abs{position:absolute}
.topbar{left:0;top:0;width:1200px;height:60px;background:var(--green);color:#fff;font-size:12px;display:flex;align-items:center;padding:0 60px}
.topbar .trend{display:flex;align-items:center;gap:10px;flex:1}
.topbar b{font-weight:700}
.topbar .trend span.t{color:#dff3c9}
.social-mini{display:flex;gap:10px;align-items:center}
.social-mini i{width:22px;height:22px;background:rgba(255,255,255,.25);display:block}
.search{width:110px;height:26px;background:rgba(255,255,255,.2);color:#e8f5e0;font-size:10px;display:flex;align-items:center;padding-left:8px;letter-spacing:1px}
.header{left:0;top:60px;width:1200px;height:90px;background:var(--yellow);display:flex;align-items:center;padding:0 60px;justify-content:space-between}
.brand{font-size:34px;font-weight:700;color:#222;display:flex;align-items:center;gap:8px}
.brand i{width:22px;height:22px;border-radius:50%;background:var(--blue);display:block}
.nav{display:flex;gap:32px;font-size:14px;font-weight:700;color:#222}
.nav .on{color:var(--blue);border-bottom:3px solid var(--blue);padding-bottom:4px}
.cat-title{left:60px;top:184px;font-size:22px;font-weight:700;color:var(--blue);letter-spacing:1px}
.photo{display:block}
.hero{left:60px;top:225px;width:799px;height:471px}
.hero .cap{position:absolute;left:0;bottom:0;width:100%;padding:16px 18px;background:linear-gradient(transparent,rgba(0,0,0,.75));color:#fff}
.hero h2{font-size:18px;font-weight:700;letter-spacing:.5px}
.hero p{font-size:11px;margin-top:6px}
.box{background:var(--white);box-shadow:0 1px 3px rgba(0,0,0,.08)}
.list{left:60px;top:714px;width:799px;height:1304px;border-top:5px solid var(--purple);padding:0 18px}
.item{display:flex;gap:20px;height:259px;padding:18px 0;border-bottom:1px solid var(--line)}
.item:last-child{border-bottom:0}
.thumb{width:372px;height:212px;flex:none;position:relative}
.play{position:absolute;left:50%;top:50%;transform:translate(-50%,-50%)}
.item h3{font-size:14px;font-weight:700;color:var(--blue);text-transform:uppercase;line-height:1.35}
.meta{font-size:10px;color:var(--muted);margin:8px 0}
.item p{font-size:12px;color:#666;line-height:1.6}
.btn{display:inline-block;margin-top:12px;background:#e6e6e6;font-size:11px;font-weight:600;color:#666;padding:8px 12px}
.latest{left:60px;top:2038px;width:799px;height:259px;border-top:5px solid var(--purple);padding:0 18px}
.bhead{font-size:13px;padding:14px 0;color:#555;border-bottom:1px solid var(--line)}
.bhead b{color:var(--purple);font-weight:700;letter-spacing:.5px}
.cards{display:flex;gap:16px;margin-top:14px}
.card{width:180px}
.card .thumb{width:180px;height:107px}
.card h4{font-size:12px;font-weight:700;margin-top:10px;line-height:1.35}
.card .meta{margin:4px 0}
.col{top:2319px;width:389px;height:892px;padding:0 18px}
.col.pop{left:60px;border-top:5px solid var(--dkgreen)}
.col.top{left:470px;border-top:5px solid var(--navy)}
.col .big{width:353px;height:234px;margin-top:10px}
.col h3{font-size:14px;font-weight:700;color:var(--blue);text-transform:uppercase;margin-top:16px;line-height:1.35}
.col p.ex{font-size:12px;color:#666;line-height:1.75}
.row{display:flex;gap:12px;padding:16px 0;border-top:1px solid var(--line)}
.row .thumb{width:40px;height:40px}
.row h5{font-size:12px;font-weight:400;color:var(--blue);line-height:1.35}
.row .meta{margin:4px 0 0}
.side{left:881px;width:259px}
.shead{background:var(--orange);color:#fff;font-size:13px;font-weight:700;letter-spacing:1px;padding:12px 16px;text-transform:uppercase}
.slist li{list-style:none;font-size:11px;color:#555;line-height:1.4;padding:12px 16px;border-bottom:1px solid var(--line)}
.slist li small{color:var(--muted);font-size:9px}
.slist li a{color:var(--blue);text-decoration:none}
.vid{width:259px;height:208px;position:relative}
.follow li{display:flex;align-items:center;gap:14px;font-size:11px;font-weight:600;letter-spacing:.5px;text-transform:uppercase}
.follow i{width:28px;height:28px;border-radius:50%;display:block;flex:none}
.footer{left:0;top:3256px;width:1200px;height:41px;background:var(--green);color:#e1f3d6;font-size:11px;display:flex;align-items:center;justify-content:space-between;padding:0 60px}
</style>
</head>
<body>

<div class="abs topbar">
  <div class="trend">
    <svg width="18" height="14" viewBox="0 0 18 14"><rect y="0" width="18" height="2" fill="#fff"/><rect y="6" width="18" height="2" fill="#fff"/><rect y="12" width="18" height="2" fill="#fff"/></svg>
    <b>TRENDING:</b><span class="t">Kaylee Vance Shoots Down Breast Implants Rumors With On...</span>
  </div>
  <div class="social-mini"><i></i><i></i><i></i><span class="search">SEARCH</span></div>
</div>

<header class="abs header">
  <div class="brand"><i></i>quorvella</div>
  <nav class="nav"><span>HOME</span><span>AFRICA ⌄</span><span>AMERICA ⌄</span><span>ASIA ⌄</span><span>AUSTRALIA ⌄</span><span class="on">EUROPE ⌄</span></nav>
</header>

<h1 class="abs cat-title">CATEGORY: EUROPE</h1>

<section class="abs hero">
  <div class="photo" role="img" aria-label="Singer performing on stage at a microphone" style="width:100%;height:100%;background:radial-gradient(circle at 50% 40%,#b98a62,#4a3224 55%,#15100d)"></div>
  <div class="cap">
    <h2>MEET THE FORMER BOARDING SCHOOL GIRL WITH AN ETHIO...</h2>
    <p>Posted by admin | Aug 28, 2016 | Europe | 0 | ☆☆☆☆☆</p>
  </div>
</section>

<section class="abs box list">
  <article class="item">
    <div class="thumb" role="img" aria-label="Singer performing at a microphone" style="background:linear-gradient(135deg,#2a1c14,#a7795a 60%,#3b2a20)">
      <svg class="play" width="56" height="56" viewBox="0 0 56 56"><circle cx="28" cy="28" r="25" fill="none" stroke="#fff" stroke-width="3"/><path d="M22 17l17 11-17 11z" fill="#fff"/></svg>
    </div>
    <div><h3>Meet the former boarding school girl with an Ethiopian mother who sang the NBR's Continental Cup 2016 theme song</h3>
    <div class="meta">by admin | Aug 28, 2016 | Europe | 0 | ☆☆☆☆☆</div>
    <p>Rising star Ivy Brisa's reworking of the Elodie Pavan classic, La Marée, will be beamed into British homes on a daily basis.</p>
    <span class="btn">READ MORE</span></div>
  </article>
  <article class="item">
    <div class="thumb" role="img" aria-label="Author standing at a podium" style="background:linear-gradient(180deg,#e8d9c8,#c9b49c 60%,#8d6f55)"></div>
    <div><h3>British author Rowan says Trevant has a right to be bigoted</h3>
    <div class="meta">by admin | Aug 28, 2016 | Europe | 0 | ☆☆☆☆☆</div>
    <p>Wizard author J.R. Rowan labeled U.S. presidential candidate Dalton Trevant bigoted after receiving the Quill/Alder Foundation Literary Service Award in New York.</p>
    <span class="btn">READ MORE</span></div>
  </article>
  <article class="item">
    <div class="thumb" role="img" aria-label="Couple holding newborn twin babies" style="background:linear-gradient(135deg,#9ab26a,#e6d5c2 50%,#c9a88a)"></div>
    <div><h3>Rocker Ronan Wade, 68, becomes dad to twin girls</h3>
    <div class="meta">by admin | Aug 28, 2016 | Europe | 0 | ☆☆☆☆☆</div>
    <p>At 68, guitarist Ronan Wade has become dad to twin girls, Gwen Jade and Ada Rose. They are his first children with wife Sadie, who is 30 years his junior and a theatre producer.</p>
    <span class="btn">READ MORE</span></div>
  </article>
  <article class="item">
    <div class="thumb" role="img" aria-label="Portrait of a bearded actor" style="background:linear-gradient(135deg,#b03a1e,#c98466 55%,#5a2a1a)">
      <svg class="play" width="56" height="56" viewBox="0 0 56 56"><circle cx="28" cy="28" r="25" fill="none" stroke="#fff" stroke-width="3"/><path d="M22 17l17 11-17 11z" fill="#fff"/></svg>
    </div>
    <div><h3>Gentle giant Buck Spenner laid to rest in Rome</h3>
    <div class="meta">by admin | Aug 28, 2016 | Europe | 0 | ☆☆☆☆☆</div>
    <p>Hundreds of family and friends have attended the funeral of Italian actor Carlo Pedrani, better known as Buck Spenner.</p>
    <span class="btn">READ MORE</span></div>
  </article>
  <article class="item">
    <div class="thumb" role="img" aria-label="Couple posing at a red carpet event" style="background:linear-gradient(135deg,#7b6a5c,#c7b8a8 50%,#3c3f4a)"></div>
    <div><h3>Gemma Mae Forde splits from boyfriend Gianni Perrone</h3>
    <div class="meta">by admin | Aug 28, 2016 | Europe | 0 | ☆☆☆☆☆</div>
    <p>Tweeting out a statement which was then retweeted by Gianni, the former Corridor Lane star said: "It is with great sadness we have decided to split up. There is nobody else involved. Although it was not an easy decision to make sometimes you realise that it is better to be friends and this is one of those times.</p>
    <span class="btn">READ MORE</span></div>
  </article>
</section>

<section class="abs box latest">
  <div class="bhead"><b>EUROPE</b> Latest</div>
  <div class="cards">
    <div class="card"><div class="thumb" role="img" aria-label="Singer on stage" style="background:linear-gradient(135deg,#2a1c14,#a7795a)"></div><h4>Meet the former boarding school girl wit...</h4><div class="meta">Aug 28, 2016</div></div>
    <div class="card"><div class="thumb" role="img" aria-label="Author at a podium" style="background:linear-gradient(180deg,#e8d9c8,#8d6f55)"></div><h4>British author Rowan says Trevant has a ...</h4><div class="meta">Aug 28, 2016</div></div>
    <div class="card"><div class="thumb" role="img" aria-label="Couple with twin babies" style="background:linear-gradient(135deg,#9ab26a,#e6d5c2)"></div><h4>ROCKER RONAN WADE, 68, BECOMES D...</h4><div class="meta">Aug 28, 2016</div></div>
    <div class="card"><div class="thumb" role="img" aria-label="Bearded actor portrait" style="background:linear-gradient(135deg,#b03a1e,#c98466)"></div><h4>Gentle giant Buck Spenner laid to rest in...</h4><div class="meta">Aug 28, 2016</div></div>
  </div>
</section>

<section class="abs box col pop">
  <div class="bhead"><b>EUROPE</b> Popular</div>
  <div class="big" role="img" aria-label="Couple posing at a red carpet event" style="background:linear-gradient(135deg,#7b6a5c,#c7b8a8 50%,#3c3f4a)"></div>
  <h3>Gemma Mae Forde splits from boyfriend Gianni Perrone</h3>
  <div class="meta">by admin | Aug 28, 2016 | Europe | 0 | ☆☆☆☆☆</div>
  <p class="ex">Tweeting out a statement which was then retweeted by Gianni, the former Corridor Lane star said: "It is with great sadness we have decided to split up. There is nobody else involved. Although it was not an easy decision to make sometimes you realise that it is better to be friends and this is one of those times.</p>
  <div style="margin-top:16px">
    <div class="row"><div class="thumb" role="img" aria-label="Bearded actor" style="background:#b8583a"></div><div><h5>Gentle giant Buck Spenner laid to rest in Rome</h5><div class="meta">by admin | Aug 28, 2016 | Europe | 0 | ☆☆☆☆☆</div></div></div>
    <div class="row"><div class="thumb" role="img" aria-label="Couple with twins" style="background:#c7c39a"></div><div><h5>ROCKER RONAN WADE, 68, BECOMES DAD TO TWIN GIRLS</h5><div class="meta">by admin | Aug 28, 2016 | Europe | 0 | ☆☆☆☆☆</div></div></div>
    <div class="row"><div class="thumb" role="img" aria-label="Singer on stage" style="background:#6a4a36"></div><div><h5>Meet the former boarding school girl with an Ethiopian mother who sang the NBR's Continental Cup 2016 theme song</h5><div class="meta">by admin | Aug 28, 2016 | Europe | 0 | ☆☆☆☆☆</div></div></div>
    <div class="row"><div class="thumb" role="img" aria-label="Author at a podium" style="background:#c9b49c"></div><div><h5>British author Rowan says Trevant has a right to be bigoted</h5><div class="meta">by admin | Aug 28, 2016 | Europe | 0 | ☆☆☆☆☆</div></div></div>
  </div>
</section>

<section class="abs box col top">
  <div class="bhead"><b>EUROPE</b> Top Rated</div>
  <div class="big" role="img" aria-label="Couple posing at a red carpet event" style="background:linear-gradient(135deg,#7b6a5c,#c7b8a8 50%,#3c3f4a)"></div>
  <h3>Gemma Mae Forde splits from boyfriend Gianni Perrone</h3>
  <div class="meta">by admin | Aug 28, 2016 | Europe | 0 | ☆☆☆☆☆</div>
  <p class="ex">Tweeting out a statement which was then retweeted by Gianni, the former Corridor Lane star said: "It is with great sadness we have decided to split up. There is nobody else involved. Although it was not an easy decision to make sometimes you realise that it is better to be friends and this is one of those times.</p>
  <div style="margin-top:16px">
    <div class="row"><div class="thumb" role="img" aria-label="Bearded actor" style="background:#b8583a"></div><div><h5>Gentle giant Buck Spenner laid to rest in Rome</h5><div class="meta">by admin | Aug 28, 2016 | Europe | 0 | ☆☆☆☆☆</div></div></div>
    <div class="row"><div class="thumb" role="img" aria-label="Couple with twins" style="background:#c7c39a"></div><div><h5>ROCKER RONAN WADE, 68, BECOMES DAD TO TWIN GIRLS</h5><div class="meta">by admin | Aug 28, 2016 | Europe | 0 | ☆☆☆☆☆</div></div></div>
    <div class="row"><div class="thumb" role="img" aria-label="Author at a podium" style="background:#c9b49c"></div><div><h5>British author Rowan says Trevant has a right to be bigoted</h5><div class="meta">by admin | Aug 28, 2016 | Europe | 0 | ☆☆☆☆☆</div></div></div>
    <div class="row"><div class="thumb" role="img" aria-label="Singer on stage" style="background:#6a4a36"></div><div><h5>Meet the former boarding school girl with an Ethiopian mother who sang the NBR's Continental Cup 2016 theme song</h5><div class="meta">by admin | Aug 28, 2016 | Europe | 0 | ☆☆☆☆☆</div></div></div>
  </div>
</section>

<aside>
  <section class="abs box side" style="top:187px;height:370px">
    <div class="shead">Recent Posts</div>
    <ul class="slist">
      <li>Why a celebrity divorce has Chinese social media buzzing <small>August 28, 2016</small></li>
      <li>Is Kavya Rao on the same page as Anaya Mehta? <small>August 28, 2016</small></li>
      <li>What the "Three-Eyed God" fears most is... <small>August 28, 2016</small></li>
      <li>The Build reveals Jena and Sara as bathroom queens, while Dev and Corin continue a week from hell <small>August 28, 2016</small></li>
      <li style="border:0">Ugly twist in Corvale's bitter divorce war <small>August 28, 2016</small></li>
    </ul>
  </section>

  <section class="abs box side" style="top:580px;height:602px">
    <div class="shead">Recent Videos</div>
    <div class="vid" role="img" aria-label="Singer at a celebrity event" style="background:linear-gradient(135deg,#1d6fb8,#4aa3e0 50%,#b98d70)">
      <svg class="play" width="56" height="56" viewBox="0 0 56 56"><circle cx="28" cy="28" r="25" fill="none" stroke="#fff" stroke-width="3"/><path d="M22 17l17 11-17 11z" fill="#fff"/></svg>
    </div>
    <ul class="slist">
      <li><a>Marina Caly's troubled sister arrested on suspicion of prostitution</a></li>
      <li>Brielle Sparks' Backseat Singalong With Jonah Corbin is Filled With Dick Jokes, High Notes &amp; Schoolgirl Uniforms</li>
      <li>Meet the former boarding school girl with an Ethiopian mother who sang the NBR's Continental Cup 2016 theme song</li>
      <li>Gentle giant Buck Spenner laid to rest in Rome</li>
      <li style="border:0">WATCH! Sizwe has a new queen B in his life</li>
    </ul>
  </section>

  <section class="abs box side" style="top:1206px;height:254px">
    <div class="shead">Recent Comments</div>
    <ul class="slist">
      <li><small>Anonymous on</small> WATCH! Sizwe has a new queen B in his life</li>
      <li><a>Fathima</a> <small>on</small> Kaylee Vance Shoots Down Breast Implants Rumors With One Hilarious Tweet</li>
      <li style="border:0"><small>Anonymous on</small> Kaylee Vance Shoots Down Breast Implants Rumors With One Hilarious Tweet</li>
    </ul>
  </section>

  <section class="abs box side" style="top:1480px;height:259px">
    <div class="shead">Categories</div>
    <ul class="slist">
      <li>Africa</li><li>America</li><li>Asia</li><li>Australia</li><li style="border:0">Europe</li>
    </ul>
  </section>

  <section class="abs box side follow" style="top:1759px;height:420px">
    <div class="shead">Follow Us</div>
    <ul class="slist">
      <li><i style="background:#b31c1c"></i>Streamora</li>
      <li><i style="background:#4fc3ef"></i>Clipvale</li>
      <li><i style="background:#35465c"></i>Blogrum</li>
      <li><i style="background:#2aa3ef"></i>Chirply</li>
      <li><i style="background:#cb2027"></i>Pinvora</li>
      <li style="border:0"><i style="background:#517fa4"></i>Snapgrid</li>
    </ul>
  </section>
</aside>

<footer class="abs footer">
  <span>© 2016 quorvella</span>
  <div class="social-mini"><i style="width:16px;height:16px"></i><i style="width:16px;height:16px"></i><i style="width:16px;height:16px"></i></div>
</footer>

</body>
</html>
```